Quorvex business card design

create modern and tech looking business card that is clean but effectively communciates that we are a cloud communications company.
Should have at minimum:
Employee Name
Postion
Phone Number
Email
website
create modern and tech looking business card that is clean but effectively communciates that we are a cloud communications company. We have two logo color schemes (attached) so would like to see designs both ways
Should have at minimum:
Employee Name
Postion
Phone Number
Email
website

```html
<!DOCTYPE html>
<html lang="en">
<head>
<meta charset="utf-8">
<title>Quorvex business cards</title>
<link rel="stylesheet" href="https://fonts.googleapis.com/css2?family=Open+Sans:wght@400;700&display=swap">
<style>
  :root {
    --backdrop: #5a5859;
    --paper: #ffffff;
    --cyan: #3bbbdf;
    --purple: #662a85;
    --green: #9bc43f;
    --ink: #111111;
    --logo-grey: #58585a;
  }
  * { box-sizing: border-box; margin: 0; padding: 0; }
  html, body { width: 1200px; height: 822px; overflow: hidden; }
  body {
    background: var(--backdrop);
    font-family: "Open Sans", Arial, sans-serif;
    position: relative;
  }
  .card {
    position: absolute;
    width: 462px;
    height: 278px;
    background: var(--paper);
    overflow: hidden;
  }
  .card--front-purple { left: 124px; top: 95px; }
  .card--back-purple  { left: 622px; top: 98px; }
  .card--front-green  { left: 128px; top: 426px; }
  .card--back-green   { left: 618px; top: 424px; }

  .scheme-purple { --accent: var(--purple); }
  .scheme-green  { --accent: var(--green); }

  .bands {
    position: absolute;
    inset: 0;
    width: 462px;
    height: 278px;
  }
  .band--cyan { fill: var(--cyan); }
  .band--accent { fill: var(--accent); }

  .brand {
    position: absolute;
    left: 32px;
    top: 121px;
    display: flex;
    align-items: center;
    gap: 10px;
  }
  .brand__mark {
    width: 16px;
    height: 16px;
    background: var(--accent);
  }
  .brand__name {
    font-size: 26px;
    font-weight: 700;
    color: var(--logo-grey);
    letter-spacing: 1px;
    line-height: 1;
  }

  .pixel {
    position: absolute;
    width: 27px;
    height: 27px;
  }
  .pixel--cyan { background: var(--cyan); }
  .pixel--accent { background: var(--accent); }

  .contact {
    position: absolute;
    right: 41px;
    top: 62px;
    text-align: right;
    list-style: none;
    color: var(--ink);
    font-size: 18px;
    line-height: 38px;
  }
  .contact__name { font-weight: 700; }
</style>
</head>
<body>

  <section class="card card--front-purple scheme-purple" aria-label="Card front, purple scheme">
    <svg class="bands" viewBox="0 0 462 278" aria-hidden="true">
      <polygon class="band--cyan" points="408,0 452,0 392,278 348,278"/>
      <polygon class="band--accent" points="462,70 462,278 426,278"/>
    </svg>
    <div class="brand"><span class="brand__mark"></span><span class="brand__name">Quorvex</span></div>
    <span class="pixel pixel--cyan" style="left:318px;top:53px"></span>
    <span class="pixel pixel--accent" style="left:434px;top:29px"></span>
    <span class="pixel pixel--accent" style="left:273px;top:127px"></span>
    <span class="pixel pixel--accent" style="left:385px;top:121px"></span>
    <span class="pixel pixel--cyan" style="left:292px;top:186px"></span>
    <span class="pixel pixel--accent" style="left:422px;top:190px"></span>
  </section>

  <section class="card card--back-purple scheme-purple" aria-label="Card back, purple scheme">
    <svg class="bands" viewBox="0 0 462 278" aria-hidden="true">
      <polygon class="band--accent" points="0,0 56,0 0,150"/>
      <polygon class="band--cyan" points="92,0 128,0 44,278 8,278"/>
      <polygon class="band--accent" points="160,0 226,0 142,278 76,278"/>
      <polygon class="band--cyan" points="96,278 134,278 148,232 110,232"/>
    </svg>
    <ul class="contact">
      <li class="contact__name">John Doe</li>
      <li>CEO</li>
      <li>+64 021 555 0147</li>
      <li>johnd@quorvex.com</li>
      <li>www.quorvex.com</li>
    </ul>
  </section>

  <section class="card card--front-green scheme-green" aria-label="Card front, green scheme">
    <svg class="bands" viewBox="0 0 462 278" aria-hidden="true">
      <polygon class="band--cyan" points="408,0 452,0 392,278 348,278"/>
      <polygon class="band--accent" points="462,70 462,278 426,278"/>
    </svg>
    <div class="brand" style="top:127px"><span class="brand__mark"></span><span class="brand__name">Quorvex</span></div>
    <span class="pixel pixel--cyan" style="left:315px;top:61px"></span>
    <span class="pixel pixel--accent" style="left:431px;top:37px"></span>
    <span class="pixel pixel--accent" style="left:270px;top:135px"></span>
    <span class="pixel pixel--accent" style="left:382px;top:129px"></span>
    <span class="pixel pixel--cyan" style="left:289px;top:194px"></span>
    <span class="pixel pixel--accent" style="left:418px;top:197px"></span>
  </section>

  <section class="card card--back-green scheme-green" aria-label="Card back, green scheme">
    <svg class="bands" viewBox="0 0 462 278" aria-hidden="true">
      <polygon class="band--accent" points="0,0 56,0 0,150"/>
      <polygon class="band--cyan" points="92,0 128,0 44,278 8,278"/>
      <polygon class="band--accent" points="160,0 226,0 142,278 76,278"/>
      <polygon class="band--cyan" points="96,278 134,278 148,232 110,232"/>
    </svg>
    <ul class="contact" style="right:38px;top:64px">
      <li class="contact__name">John Doe</li>
      <li>CEO</li>
      <li>+64 021 555 0147</li>
      <li>johnd@quorvex.com</li>
      <li>www.quorvex.com</li>
    </ul>
  </section>

</body>
</html>
```